Business Card template designs

We need a lot of Business card designs.
Your designs will get exposure on our newly opened business-card printing website.
We are committed to quality of paper and packages we use, so they will come up very fancy.

Here is your advantage. We will put the profile of the graphic designer on our site so that you can showcase your designs to people around the world and in Japan.

A profile is not mandatory, although we encourage graphic designers to have a profile to get continuous work in the future.
We are looking forward to having many good designs.

The right of the use of design will be owned by us.
The design may be used to the products other than
business cards.

Target Market(s)

designer,photographer,creator,artist

Industry/Entity Type

Printing

Contact Information for Business Card

The back design is important.
Please check the reference file.

Requirements
Must have
• Please include the following, required information on your business card designs.
• Name: Haruka Tanabe
• Title: Designer
• Web: https://www.korimo.co.jp/kr/
• Address: 4-17 Kitaharazono-Cho Nerima-ku, Tokyo
• Email: info@kkorimo.com
• Phone: 03 6184 3970
• Mobile: 070 4213 6087
• * For Japanese sites, we will convert the text portion to Japanese characters.
• * In case of 28mmx70mm only include Name,Enail,Phone and SNS account(https://www.facebook.com/kkorimo.com)
• 1. colorful
• 2. simple
• 3. natural
• 4. modern
• 5. cool
• 6. sporty
• Please make variations of the same image with 3-6
• different colors / patterns for one design so that
• customers can compare and choose.
• If you want to use a same picture, please make make
• copies and paste on each different types of design.
Nice to have
• You may also use, the following non-required information.
• Company Name: Korimo, Inc.
• Fax: 03-6471-2093
• Open space for company logo

```html
<!DOCTYPE html>
<html lang="en">
<head>
<meta charset="utf-8">
<title>Korimo Business Card</title>
<link href="https://fonts.googleapis.com/css2?family=Roboto:wght@400;500;700&display=swap" rel="stylesheet">
<style>
  :root {
    --backdrop: #8f9092;
    --brand-blue: #0b2a78;
    --panel: #e9eaee;
    --panel-edge: #8b8e97;
    --ink: #262626;
    --ink-soft: #3c3c3c;
    --logo-white: #e6e8ee;
    --web-grey: #c9cde0;
  }
  * { box-sizing: border-box; margin: 0; padding: 0; }
  html, body {
    width: 1105px; height: 1200px; overflow: hidden;
    background: var(--backdrop);
    font-family: "Roboto", Arial, sans-serif;
  }
  .card {
    position: absolute; left: 182px; width: 747px; height: 427px;
    background: var(--brand-blue); overflow: hidden;
  }
  .card--front { top: 119px; }
  .card--back { top: 635px; }

  .wordmark {
    position: absolute; left: 0; width: 100%; text-align: center;
    color: var(--logo-white); font-weight: 500; font-size: 88px;
    letter-spacing: 2px; line-height: 1;
  }
  .card--front .wordmark { top: 72px; }
  .card--back .wordmark { top: 184px; }

  .info-panel { position: absolute; left: 0; top: 243px; width: 747px; height: 184px; }

  .holder { position: absolute; left: 32px; color: var(--ink); }
  .holder__name { position: absolute; top: 270px; font-size: 24px; font-weight: 500; white-space: nowrap; }
  .holder__title { position: absolute; top: 302px; font-size: 19px; color: var(--ink-soft); white-space: nowrap; }
  .holder__company { position: absolute; top: 339px; font-size: 17px; font-weight: 700; white-space: nowrap; }
  .holder__address { position: absolute; top: 362px; font-size: 17.5px; line-height: 26px; color: var(--ink-soft); white-space: nowrap; }

  .contacts { position: absolute; right: 30px; top: 266px; list-style: none; color: var(--ink-soft); }
  .contacts li {
    display: flex; justify-content: flex-end; align-items: center; gap: 10px;
    height: 28.5px; font-size: 18.5px; white-space: nowrap;
  }
  .contacts svg { width: 18px; height: 18px; fill: var(--ink); flex: none; }

  .back-web {
    position: absolute; left: 0; width: 100%; top: 361px; text-align: center;
    color: var(--web-grey); font-size: 17px; letter-spacing: .3px;
  }
</style>
</head>
<body>

<section class="card card--front" aria-label="Card front">
  <div class="wordmark">Korimo</div>

  <svg class="info-panel" viewBox="0 0 747 184" aria-hidden="true">
    <path d="M0 0 H672 A75 46 0 0 1 747 46 V184 H0 Z" fill="var(--panel)"/>
    <path d="M540 1.5 H672 A75 46 0 0 1 745.5 46" fill="none" stroke="var(--panel-edge)" stroke-width="4"/>
  </svg>

  <div class="holder">
    <p class="holder__name">Haruka Tanabe</p>
    <p class="holder__title">Designer</p>
    <p class="holder__company">Korimo, Inc.</p>
    <p class="holder__address">4-17 Kitaharazono-Cho<br>Nerima-ku, Tokyo</p>
  </div>

  <ul class="contacts">
    <li>03 6184 3970
      <svg viewBox="0 0 20 20"><path d="M2 8c0-3 4-5 8-5s8 2 8 5l-3 1-1-2H6L5 9 2 8zM5 10h10l2 7H3l2-7zm5 2a2 2 0 100 4 2 2 0 000-4z"/></svg>
    </li>
    <li>070 4213 6087
      <svg viewBox="0 0 20 20"><path d="M6 1h8a1 1 0 011 1v16a1 1 0 01-1 1H6a1 1 0 01-1-1V2a1 1 0 011-1zm1 3v11h6V4H7zm3 12a1 1 0 100 2 1 1 0 000-2z"/></svg>
    </li>
    <li>03-6471-2093
      <svg viewBox="0 0 20 20"><path d="M5 2h10v5H5V2zM2 8h16v7h-3v3H5v-3H2V8zm5 6v2h6v-2H7z"/></svg>
    </li>
    <li>info@kkorimo.com
      <svg viewBox="0 0 20 20"><path d="M2 5h16v1l-8 5-8-5V5zm0 3l8 5 8-5v7H2V8z"/></svg>
    </li>
    <li>www.korimo.co.jp/kr
      <svg viewBox="0 0 20 20"><circle cx="10" cy="10" r="8"/><path d="M6 6c2 0 3 1 2 3s1 2 0 4M13 5c-1 2 1 3 2 3M12 15c0-2 2-2 3-3" stroke="var(--panel)" stroke-width="1.4" fill="none"/></svg>
    </li>
  </ul>
</section>

<section class="card card--back" aria-label="Card back">
  <div class="wordmark">Korimo</div>
  <p class="back-web">www.korimo.co.jp/kr</p>
</section>

</body>
</html>
```